Red Sea Boat trips in need of Business Card for Private Boat Tours

We need a Business card for a new business set-up in Egypt on the Red Sea for private snorkelling and boat excursions to one of the world's most beautiful reefs. We have wording logo already set-up which matches the boat but we need business cards to be bright and colourful with pictures of boat

Industry/Entity Type

Tourism

Contact Information for Business Card

Two Silver Herons (font provided) Boat Trips

```html
<!DOCTYPE html>
<html lang="en">
<head>
<meta charset="utf-8">
<title>Two Silver Herons – Business Card</title>
<link rel="stylesheet" href="https://fonts.googleapis.com/css2?family=Lato:ital,wght@0,400;0,700;0,900;1,400&display=swap">
<style>
  :root {
    --page-bg: #1e1e1e;
    --card-bg: #ffffff;
    --ink: #111111;
    --ink-soft: #444444;
    --rule: #1a1a1a;
    --sea-deep: #1f4fa8;
    --sea-mid: #2a8fb0;
    --sea-light: #6fc3cf;
    --reef: #6b6a4a;
    --sky: #a9c6dc;
    --name-light: #ffffff;
  }
  * { margin: 0; padding: 0; box-sizing: border-box; }
  html, body {
    width: 1047px; height: 1200px; overflow: hidden;
    background: var(--page-bg);
    font-family: "Lato", sans-serif;
  }
  .card {
    position: absolute; left: 151px; width: 744px; height: 424px;
    border-radius: 20px; overflow: hidden;
  }
  .card--front { top: 120px; background: var(--card-bg); color: var(--ink); }
  .card--back { top: 634px; }

  .brand-name {
    position: absolute; right: 54px; top: 58px;
    font-weight: 900; font-size: 40px; color: var(--ink); letter-spacing: 0.5px;
  }
  .person { position: absolute; left: 46px; top: 224px; }
  .person__name { font-weight: 700; font-size: 31px; letter-spacing: 0.5px; line-height: 1; }
  .person__role { font-style: italic; font-size: 18px; color: var(--ink-soft); margin-top: 6px; }
  .divider {
    position: absolute; left: 46px; right: 54px; top: 290px;
    height: 2px; background: var(--rule);
  }
  .contacts { position: absolute; left: 46px; top: 327px; list-style: none; }
  .contacts li {
    display: flex; align-items: center; gap: 12px;
    font-size: 17px; color: var(--ink-soft); height: 26px;
  }
  .contacts svg { width: 16px; height: 16px; fill: var(--ink); flex: none; }
  .address {
    position: absolute; right: 54px; top: 326px; text-align: right;
    font-size: 17px; color: var(--ink-soft); line-height: 25.5px;
  }

  .scene {
    position: absolute; inset: 0;
    background:
      linear-gradient(180deg, rgba(255,255,255,0.15) 0%, rgba(0,0,0,0) 40%, rgba(30,40,30,0.25) 100%),
      linear-gradient(90deg, var(--sky) 0%, var(--sea-light) 18%, var(--sea-mid) 32%, var(--reef) 48%, var(--sea-light) 62%, var(--reef) 78%, var(--sea-deep) 88%, var(--sea-deep) 100%);
  }
  .back-name {
    position: absolute; left: 0; right: 0; top: 182px; text-align: center;
    font-weight: 900; font-size: 54px; color: var(--name-light); letter-spacing: 0.5px;
  }
</style>
</head>
<body>
  <section class="card card--front">
    <div class="brand-name">Two Silver Herons</div>
    <div class="person">
      <div class="person__name">MARCUS HALE</div>
      <div class="person__role">Founder &amp; Dirctor</div>
    </div>
    <div class="divider"></div>
    <ul class="contacts">
      <li>
        <svg viewBox="0 0 16 16"><path d="M3.6 1.5l2.3 2.6-1.2 1.8c.9 2 2.4 3.5 4.4 4.4l1.8-1.2 2.6 2.3-1.3 2.2C7 13.3 2.7 9 2.4 3.1z"/></svg>
        (123) 456-7890
      </li>
      <li>
        <svg viewBox="0 0 16 16"><path d="M4.5 1h7a1 1 0 0 1 1 1v12a1 1 0 0 1-1 1h-7a1 1 0 0 1-1-1V2a1 1 0 0 1 1-1zm.6 2v8.5h5.8V3zM8 12.4a.8.8 0 1 0 0 1.6.8.8 0 0 0 0-1.6z"/></svg>
        (123) 456-7890
      </li>
      <li>
        <svg viewBox="0 0 16 16"><path d="M1.5 3.5h13v9h-13zm1.2 1.2v.3L8 8.6l5.3-3.6v-.3zm0 1.8v4.8h10.6V6.5L8 10.1z"/></svg>
        info@twosilverherons.com
      </li>
    </ul>
    <div class="address">
      Street Address Here<br>
      City, State, ZIP 12345<br>
      www.twosilverherons.com
    </div>
  </section>

  <section class="card card--back">
    <div class="scene" role="img" aria-label="Photo collage: a white motor boat on the Red Sea, coral reef with fish, a scuba diver among bubbles and a freediver in deep blue water"></div>
    <div class="back-name">Two Silver Herons</div>
  </section>
</body>
</html>
```